Borealis Fuel Industry Expo

I need to have a banner made up for a tradeshow booth backdrop. I don't want there to be any hiring information. This is to promote to other organizations who we are as a remote medical company. We provide medical support to remote camps and vessels. We employ EMT's, Paramedics, Physician Assistants, Off-site Medical Doctor. Our website is corvanimed.com

```html
<!DOCTYPE html>
<html lang="en">
<head>
<meta charset="UTF-8">
<title>Corvani Medical – Booth Backdrop</title>
<link rel="stylesheet" href="https://fonts.googleapis.com/css2?family=Open+Sans:wght@600;700;800&family=Roboto:wght@400&display=swap">
<style>
  :root {
    --stage: #6b6b6b;
    --paper: #ffffff;
    --paper-shade: #ececec;
    --navy: #0c0f7a;
    --red: #c20c1c;
    --red-deep: #8f0812;
    --white: #ffffff;
  }
  * { box-sizing: border-box; margin: 0; padding: 0; }
  html, body {
    width: 1200px;
    height: 840px;
    overflow: hidden;
    background: var(--stage);
  }
  .backdrop {
    position: absolute;
    left: 170px;
    top: 20px;
    width: 860px;
    height: 800px;
    background:
      linear-gradient(135deg, transparent 0 30%, rgba(255,255,255,0.9) 30% 34%, transparent 34% 100%),
      linear-gradient(135deg, var(--paper) 0%, var(--paper-shade) 45%, var(--paper) 60%, var(--paper-shade) 100%);
    overflow: hidden;
    font-family: "Open Sans", sans-serif;
    text-align: center;
  }
  .brand {
    position: absolute;
    top: 78px;
    left: 0;
    right: 0;
    display: flex;
    justify-content: center;
    align-items: center;
    gap: 18px;
  }
  .brand-dot {
    width: 112px;
    height: 112px;
    border-radius: 50%;
    background: var(--red);
  }
  .brand-name {
    font-weight: 800;
    font-size: 84px;
    line-height: 1;
    color: var(--navy);
    letter-spacing: -1px;
  }
  .lead {
    position: absolute;
    top: 250px;
    left: 0;
    right: 0;
    font-weight: 800;
    font-size: 52px;
    color: var(--navy);
    letter-spacing: -1px;
    line-height: 1;
  }
  .headline {
    position: absolute;
    top: 315px;
    left: 0;
    right: 0;
    font-weight: 800;
    font-size: 76px;
    color: var(--red);
    letter-spacing: -1.5px;
    line-height: 1;
  }
  .tagline {
    position: absolute;
    top: 418px;
    left: 50%;
    transform: translateX(-50%);
    width: 510px;
    height: 46px;
    border-radius: 23px;
    background: var(--navy);
    color: var(--white);
    font-weight: 800;
    font-size: 27px;
    line-height: 46px;
    letter-spacing: -0.3px;
  }
  .services {
    position: absolute;
    top: 500px;
    left: 90px;
    right: 60px;
    display: flex;
    justify-content: space-between;
    list-style: none;
  }
  .service {
    width: 160px;
    display: flex;
    flex-direction: column;
    align-items: center;
  }
  .service-icon {
    width: 66px;
    height: 66px;
    border-radius: 50%;
    background: var(--red);
    box-shadow: inset 0 0 0 3px var(--red), inset 0 0 0 5px var(--white);
  }
  .service-label {
    margin-top: 12px;
    font-weight: 600;
    font-size: 18px;
    line-height: 1.35;
    color: var(--navy);
    letter-spacing: -0.4px;
  }
  .web-band {
    position: absolute;
    top: 665px;
    left: 0;
    right: 0;
    height: 58px;
    background: linear-gradient(90deg, var(--red-deep) 0%, var(--red) 30%, var(--red) 100%);
    color: var(--white);
    font-family: "Roboto", sans-serif;
    font-size: 30px;
    line-height: 58px;
    letter-spacing: 8px;
  }
</style>
</head>
<body>
  <main class="backdrop">
    <header class="brand">
      <div class="brand-dot"></div>
      <span class="brand-name">CORVANI</span>
    </header>

    <p class="lead">WE PROVIDE</p>
    <h1 class="headline">MEDICAL SUPPORT</h1>
    <p class="tagline">TO REMOTE CAMPS AND VESSELS</p>

    <ul class="services">
      <li class="service">
        <div class="service-icon" role="img" aria-label="Icon of a caregiver held in open hands"></div>
        <span class="service-label">WE EMPLOY<br>EMT'S</span>
      </li>
      <li class="service">
        <div class="service-icon" role="img" aria-label="Star of life emergency medical icon"></div>
        <span class="service-label">PARAMEDICS</span>
      </li>
      <li class="service">
        <div class="service-icon" role="img" aria-label="Icon of a physician assistant with a medical bag"></div>
        <span class="service-label">PHYSICIAN<br>ASSISTANTS</span>
      </li>
      <li class="service">
        <div class="service-icon" role="img" aria-label="Icon of a doctor with a stethoscope"></div>
        <span class="service-label">OFF-SITE<br>MEDICAL DOCTOR</span>
      </li>
    </ul>

    <div class="web-band">corvanimed.com</div>
  </main>
</body>
</html>
```